Jetzt starten So funktioniert'sAuf die Visitenkarte soll ein Logo bzw. eine Grafik dargestellt werden, welche ebenfalls auf der Website und dem Flyer genutzt werden soll wird es hier als Logo bezeichnet. Die Grafik soll ein Labyrinth und eine Person in einer scheinbar aussichtsloser Lage darstellen mit der Frage „WOGEMA gefä..
16Stein, Weg, Füße, Baby o. Kind....Sonne... Vielleicht fällt Ihnen auch etwas besseres ein. Evtl. ein Slogan wie z. B. -Kinderbetreuung mit ❤️ - Hier steht das Kind im Mittelpunkt. -Jedes Kind ist einzigartig? Oder - „Hilf mir es selbst zu tun“ aber vielleicht anders formuliert. (..
40Es müssen für zwei Geschäfte Visitenkarten, Briefpapier (A4) und Kassenkassenbelege (A6) erstellt werden. Logo und Typo im Anhang. Ein Farbkonzept besteht noch nicht. Die Idee geht in Richtung Bordeaux-Rot. Generell: (1) Sieht erstmal nach viel Beschreibung aus, bitte nicht entmutigen lass..
118Schlichtes aber direkt erkennbares Design. Fang neu an , Gesundheit und Ernährungsberatung ( gut lesbar , elegant) Marlene Osterkamp-Riedel ( nicht so groß ) Grau ; Grün Töne und gerne etwas rosa Infos wie Adresse und E-Mail vielleicht in jeweilige Blöcke am unteren Rand
30Wir benötigen, passend zu unserem neuen Logo, Geschäftspapier, Visitenkarten und eine Vorlage für eine PowerPoint Präsentation (Hintergrunds-Seite)

```html
<!DOCTYPE html>
<html lang="de">
<head>
<meta charset="utf-8">
<title>Berno Valic – Geschäftsausstattung</title>
<link href="https://fonts.googleapis.com/css2?family=Open+Sans:wght@400;600;700&display=swap" rel="stylesheet">
<style>
  :root {
    --canvas: #ececec;
    --paper: #ffffff;
    --card: #d8d8d8;
    --red: #d2232a;
    --navy: #2b2f78;
    --ink: #333333;
    --deco: #f1f1f1;
    --deco-card: #e2e2e2;
  }
  * { margin: 0; padding: 0; box-sizing: border-box; }
  html, body { width: 1183px; height: 1200px; overflow: hidden; }
  body {
    background: var(--canvas);
    font-family: "Open Sans", Arial, sans-serif;
    color: var(--ink);
    position: relative;
  }
  .letterhead {
    position: absolute; left: 30px; top: 50px;
    width: 778px; height: 1100px;
    background: var(--paper);
    overflow: hidden;
    box-shadow: 0 4px 18px rgba(0,0,0,.12);
  }
  .pattern-band {
    position: absolute; left: 0; top: 20px;
    width: 740px; height: 70px;
    background: linear-gradient(90deg, var(--deco), #f6f6f6 60%, var(--deco));
  }
  .side-panel {
    position: absolute; top: 420px;
    width: 115px; height: 455px;
    background: linear-gradient(180deg, var(--deco), #f6f6f6);
  }
  .side-panel--left { left: 0; }
  .side-panel--right { right: 0; }
  .sender-line {
    position: absolute; left: 44px; top: 178px;
    font-size: 8px; font-weight: 700; color: var(--ink);
  }
  .brand { position: absolute; }
  .brand__name {
    display: flex; align-items: center; gap: 8px;
    font-weight: 600; color: var(--navy);
    white-space: nowrap;
  }
  .brand__mark { display: inline-block; background: var(--red); }
  .brand__services { font-weight: 600; white-space: nowrap; }
  .brand__services .accent { color: var(--red); }
  .brand__services .plain { color: var(--navy); }
  .letterhead .brand { left: 435px; top: 140px; }
  .letterhead .brand__name { font-size: 26px; }
  .letterhead .brand__mark { width: 10px; height: 10px; }
  .letterhead .brand__services { font-size: 8.5px; margin-top: 3px; }
  .contact { font-weight: 600; line-height: 1.55; }
  .contact .street { color: var(--red); }
  .contact .phone { color: var(--navy); }
  .letterhead .contact { position: absolute; left: 435px; top: 240px; font-size: 9px; }
  .bank-details {
    position: absolute; left: 432px; top: 940px;
    font-size: 8.5px; font-weight: 600; line-height: 1.6;
    color: var(--navy);
  }
  .bank-details .tax { margin-top: 12px; }

  .business-card {
    position: absolute; left: 843px; top: 470px;
    width: 310px; height: 200px;
    background: var(--card);
    overflow: hidden;
    box-shadow: 0 4px 14px rgba(0,0,0,.18);
  }
  .business-card .pattern-band {
    top: 10px; left: 0; width: 290px; height: 40px;
    background: linear-gradient(90deg, var(--deco-card), #dddddd);
  }
  .business-card .pattern-band--low { top: 158px; left: 0; width: 270px; }
  .business-card .brand { left: 36px; top: 62px; }
  .business-card .brand__name { font-size: 22px; }
  .business-card .brand__mark { width: 8px; height: 8px; }
  .business-card .brand__services { font-size: 7.5px; margin-top: 2px; }
  .business-card .contact { position: absolute; left: 36px; top: 118px; font-size: 7.5px; }
</style>
</head>
<body>
  <section class="letterhead" aria-label="Briefbogen">
    <div class="pattern-band" role="img" aria-label="Dekorative Zeichenreihe aus hellgrauen Satzzeichen"></div>
    <div class="side-panel side-panel--left" role="img" aria-label="Große hellgraue Klammer als Dekor"></div>
    <div class="side-panel side-panel--right" role="img" aria-label="Große hellgraue Klammer als Dekor"></div>

    <p class="sender-line">Berno Valic | Lindenstieg 7, 24103 Kiel</p>

    <div class="brand">
      <div class="brand__name">Berno Valic<span class="brand__mark"></span></div>
      <div class="brand__services"><span class="accent">*Korrektorat</span> <span class="plain">|</span> <span class="accent">Texterstellung*</span> <span class="plain">ghostwriting*</span></div>
    </div>

    <div class="contact">
      <div class="street">* Lindenstieg 7 _ 24103 Kiel</div>
      <div class="phone">Tel. 04 31 | 7 42 19 55 | b.valic@mailpost.de</div>
    </div>

    <div class="bank-details">
      <div>Nordbank Kiel eG</div>
      <div>Kto.-Nr. 40 218 733 – BLZ 210 500 12</div>
      <div>IBAN DE4721050012004021873300 · BIC NORDDEK1KIE</div>
      <div class="tax">USt-IdNr.: DE318275046</div>
    </div>
  </section>

  <section class="business-card" aria-label="Visitenkarte">
    <div class="pattern-band" role="img" aria-label="Dekorative Zeichenreihe aus hellen Satzzeichen"></div>
    <div class="pattern-band pattern-band--low" role="img" aria-label="Dekorative Zeichenreihe aus hellen Satzzeichen"></div>

    <div class="brand">
      <div class="brand__name">Berno Valic<span class="brand__mark"></span></div>
      <div class="brand__services"><span class="accent">*Korrektorat</span> <span class="plain">|</span> <span class="accent">Texterstellung*</span> <span class="plain">ghostwriting*</span></div>
    </div>

    <div class="contact">
      <div class="street">* Lindenstieg 7 _ 24103 Kiel</div>
      <div class="phone">Tel. 04 31 | 7 42 19 55 | b.valic@mailpost.de</div>
    </div>
  </section>
</body>
</html>
```